Cover design brief for the “Lanterns along the river” collection

This collection aims to publish articles by several authors who are practitioners specializing in sociocracy, a participatory mode of governance that is highly innovative, and even quite subversive of the autocratic way in which companies and public institutions operate. However, this method has been widely and increasingly implemented since its initial development in the Netherlands in the 1970s and 80s. It is currently of particular interest to non-profit and cooperative organizations, citizen projects and intentional communities, as well as IT work teams (due to its proximity to the spirit of Agile methods).
The content is intellectually demanding. It won't be a matter of popularization for promotional purposes, but rather of subjects for reflection or in-depth analysis of practices, and feedback from field experience. Nor is it an academic journal.
The language used for these publications is French.
The target audience is French-speaking Europe and Canada.

Target Market(s)

The collection is aimed both at other practitioners of this method who want to develop their knowledge, and at people interested in the subjects of collective intelligence, cooperation and organization, in response to social, ecological and/or political concerns.

Industry/Entity Type

Training and consultancy

Font styles to use
Sans Serif

Requirements
Must have
• The name of the collection: Lanterns along the river - Weaving a quieter commons Each volume will mention the name of the collection as well as the theme of the volume. First one: Volume 1 - Mapping hidden currents within shared endeavours. Selection criteria: - A singular, recurring visual identity for the volumes in the collection, highlighting its theme. - Appeal to potential readers; arouse curiosity. - Good readability of the text (title and subtitle, authors; presentation on back cover). - Simplicity of design variation for the cover of subsequent volumes (changing only the text). - Reasonable price in relation to a hoped-for circulation of between 100 and 300 copies per volume (the theme is linked to a niche that is still fairly narrow in the French-speaking world).
Nice to have
• Suggested graphic design directions If you have another direction to suggest with convincing arguments, we're open to your proposal. - The name of the collection, and in particular "Lanterns along the river", will be visible at first glance. - The overall visual impression is one of movement and dynamism. - The style will be based on illustration work, such as sketchnotes. - The tone is playful and humorous. For example, it may mirror back to the potential reader the cultural clichés and social norms about power that make the theme "lanterns along the river" a challenge to his or her imagination. As stated in the preface to Volume 1: "Most people are used to social environments where the choice is limited to suffering or fighting against powers that seek in a multitude of ways to put us at their service..."

```html
<!DOCTYPE html>
<html lang="en">
<head>
<meta charset="utf-8">
<title>Lanterns along the river – Volume 1</title>
<link rel="stylesheet" href="https://fonts.googleapis.com/css2?family=Archivo+Black&family=Montserrat:ital,wght@0,600;0,700;1,600&display=swap">
<style>
  :root {
    --paper: #ffffff;
    --ink: #2b2b2b;
    --orange: #f26a1b;
    --orange-deep: #e0501a;
    --orange-light: #ff9a3c;
    --glow: #fbd7bb;
  }
  * { margin: 0; padding: 0; box-sizing: border-box; }
  html, body { width: 750px; height: 1200px; overflow: hidden; background: var(--paper); }
  .cover {
    position: relative;
    width: 750px;
    height: 1200px;
    background: var(--paper);
    overflow: hidden;
    text-align: center;
  }
  .collection-tagline {
    position: absolute;
    top: 28px; left: 0; right: 0;
    font-family: "Montserrat", sans-serif;
    font-style: italic;
    font-weight: 600;
    font-size: 25px;
    line-height: 34px;
    letter-spacing: 1px;
    color: var(--ink);
    text-transform: uppercase;
  }
  .title {
    font-family: "Archivo Black", sans-serif;
    font-weight: 400;
    text-transform: uppercase;
  }
  .title-line {
    position: absolute;
    left: 0; right: 0;
    display: block;
    font-size: 84px;
    line-height: 100px;
    letter-spacing: 2px;
    background: linear-gradient(180deg, var(--orange-light) 0%, var(--orange) 55%, var(--orange-deep) 100%);
    -webkit-background-clip: text;
    background-clip: text;
    color: transparent;
  }
  .title-top { top: 145px; }
  .title-bottom { top: 318px; }
  .title-join {
    position: absolute;
    top: 250px; left: 0; right: 0;
    height: 56px;
    display: flex;
    align-items: center;
    justify-content: center;
    gap: 28px;
  }
  .title-join .rule {
    width: 150px;
    height: 3px;
    background: var(--orange);
  }
  .title-join .join-word {
    font-size: 46px;
    line-height: 56px;
    letter-spacing: 3px;
    background: linear-gradient(180deg, var(--orange-light) 0%, var(--orange) 55%, var(--orange-deep) 100%);
    -webkit-background-clip: text;
    background-clip: text;
    color: transparent;
  }
  .volume {
    position: absolute;
    top: 442px; left: 0; right: 0;
    font-family: "Montserrat", sans-serif;
    font-weight: 700;
    font-size: 30px;
    line-height: 40px;
    color: var(--orange);
    text-transform: uppercase;
  }
  .volume-theme {
    position: absolute;
    top: 500px; left: 80px; right: 80px;
    padding: 6px 8px;
    border: 3px solid var(--orange);
    font-family: "Montserrat", sans-serif;
    font-weight: 700;
    font-size: 17px;
    line-height: 24px;
    color: var(--ink);
    text-transform: uppercase;
    white-space: nowrap;
  }
  .illustration {
    position: absolute;
    top: 560px; left: 40px;
    width: 670px; height: 520px;
    background:
      radial-gradient(ellipse 38% 55% at 50% 38%, var(--orange) 0%, var(--orange-light) 35%, var(--glow) 65%, rgba(255,255,255,0) 100%),
      linear-gradient(180deg, rgba(255,255,255,0) 0%, rgba(255,255,255,0) 62%, rgba(43,43,43,0.55) 82%, rgba(255,255,255,0) 100%);
  }
  .authors {
    position: absolute;
    top: 1112px; left: 0; right: 0;
    font-family: "Montserrat", sans-serif;
    font-weight: 600;
    font-size: 27px;
    line-height: 36px;
    letter-spacing: 1px;
    color: var(--ink);
    text-transform: uppercase;
  }
</style>
</head>
<body>
  <main class="cover">
    <p class="collection-tagline">Weaving a quieter commons</p>

    <h1 class="title">
      <span class="title-line title-top">Lanterns</span>
      <span class="title-join">
        <span class="rule"></span>
        <span class="join-word">Along</span>
        <span class="rule"></span>
      </span>
      <span class="title-line title-bottom">The River</span>
    </h1>

    <p class="volume">Volume 1</p>
    <p class="volume-theme">Mapping hidden currents within shared endeavours</p>

    <div class="illustration" role="img" aria-label="Sketched orange cityscape of towers rising like a flame, with a circle of standing silhouetted figures around a central person in the foreground"></div>

    <p class="authors">Lucien Morvan, Edwin Hale</p>
  </main>
</body>
</html>
```